Heavy Equipment Service Technician

K&T Equipment Corp. is a family owned industry leader that’s been supplying construction equipment, tractors and landscaping gear to Southern Connecticut for the past 81 years. Located on Route 9 in Orange, we help home builders, site excavators, road builders, municipalities, landscapers, home owners and many more. We believe we can make work fun and easy by supplying new and used equipment, equipment rentals, service, parts and advice. Our fast paced service department is ready to expand! We are looking for a Heavy Equipment Service Technician, Experience Required.

QUALIFICATIONS AND SKILL:

· Must have a valid driver’s license.

· Must be reliable, hard working and have a professional work ethic.

· Must own tools and have the ability to work independently.

· Must have the ability to lift, push, pull 70+ pounds, climb heavy. equipment safely, bend and kneel.

· Must be able to perform basic equipment service: ie: filters, oils, inspections.

· Must possess a willingness to learn and grow.

· Must provide own tools.

RESPONSIBILITIES AND DUTIES:

· Perform scheduled services on heavy equipment and tractors.

· Perform final assembly of tractors.

· Perform body work on equipment.

· Perform minor welding on equipment and tractors.

· Keep work space clean of all debris.

Hi, This, is my first time using Mint Lantern! I am looking to design a new web page on our website that I can direct prospective employees. This webpage I want to look very professional to attract new employees. I am hoping to show off the wonderful benefits we offer, the fun work place and a great place to grow.

```html
<!DOCTYPE html>
<html lang="en">
<head>
<meta charset="utf-8">
<title>K&amp;T Equipment Corp. – Careers</title>
<link rel="stylesheet" href="https://fonts.googleapis.com/css2?family=Roboto+Slab:wght@400;500;700;800&family=Poppins:wght@400;500;600;700&display=swap">
<style>
:root{
  --yellow:#ffd200;
  --dark:#1c1c1e;
  --topbar:#231f20;
  --ink:#222;
  --body:#555;
  --light:#f1f1f1;
  --white:#fff;
  --slab:"Roboto Slab","Georgia",serif;
}
*{box-sizing:border-box;margin:0;padding:0}
html,body{width:1200px;height:3569px;overflow:hidden}
body{position:relative;font-family:"Poppins",sans-serif;color:var(--body);background:var(--white)}
.abs{position:absolute}

/* top bar */
.topbar{left:0;top:0;width:1200px;height:36px;background:var(--topbar)}
.topbar-address{left:512px;top:10px;color:var(--white);font-size:11px;display:flex;align-items:center;gap:8px;white-space:nowrap;z-index:2}
.topbar-social{left:826px;top:0;width:213px;height:36px;background:var(--yellow);clip-path:polygon(14px 0,100% 0,100% 100%,0 100%)}
.social-set{display:flex;gap:9px}
.social-set span{width:19px;height:19px;background:var(--white);border-radius:3px;display:block}
.topbar-icons{left:869px;top:8px}

/* header */
.brand-box{left:162px;top:0;width:133px;height:139px;background:var(--white);display:flex;flex-direction:column;align-items:center;justify-content:center;gap:8px;z-index:1}
.brand-box .dot{width:46px;height:46px;border-radius:50%;background:var(--yellow)}
.brand-box .name{font-family:var(--slab);font-weight:700;font-size:15px;color:var(--ink);text-align:center;line-height:1.15}
.contact-chip{display:flex;align-items:center;gap:12px}
.contact-chip .ring{width:42px;height:42px;border:2px solid #2d2d40;border-radius:50%;display:flex;align-items:center;justify-content:center}
.contact-chip .label{font-family:var(--slab);font-weight:500;font-size:18px;color:var(--ink);line-height:1.1}
.contact-chip .value{font-size:12px;color:#333}
.chip-mail{left:589px;top:64px}
.chip-phone{left:873px;top:64px}

/* nav */
.mainnav{left:0;top:139px;width:1200px;height:45px;background:var(--yellow)}
.mainnav a{position:absolute;top:12px;font-family:var(--slab);font-weight:500;font-size:15px;color:var(--white);text-decoration:none}

/* hero */
.hero{left:0;top:184px;width:1200px;height:462px;background:linear-gradient(100deg,#5a1a1e 0%,#7c2a2c 22%,#3b3c44 50%,#2b3a55 72%,#595d63 100%)}
.hero::after{content:"";position:absolute;inset:0;background:rgba(0,0,0,.38)}
.hero h1{position:absolute;z-index:1;left:0;width:1200px;top:142px;text-align:center;font-family:var(--slab);font-weight:700;font-size:54px;line-height:52px;color:var(--white)}
.hero .arrow{position:absolute;z-index:1;top:214px;width:34px;height:34px;border-radius:50%;display:flex;align-items:center;justify-content:center}
.hero .prev{left:35px;background:#3c3c3c}
.hero .next{left:1124px;background:var(--yellow)}

/* welcome */
.badge{left:148px;top:713px;width:147px;height:34px;background:var(--dark);border-radius:17px;color:var(--yellow);font-family:var(--slab);font-weight:700;font-size:16px;display:flex;align-items:center;justify-content:center}
.welcome-title{left:160px;top:756px;font-family:var(--slab);font-weight:800;font-size:37px;line-height:37px;color:var(--ink)}
.welcome-text{left:160px;top:845px;width:455px;font-size:11.2px;line-height:18.7px;text-align:justify;color:#555}
.btn{background:var(--yellow);color:var(--white);font-weight:700;font-size:12px;border-radius:20px;display:flex;align-items:center;justify-content:center;text-transform:uppercase}
.welcome-btn{left:160px;top:1025px;width:117px;height:35px}
.welcome-photo{left:669px;top:712px;width:370px;height:347px;background:linear-gradient(170deg,#d8d2c2 0%,#bdb9a6 30%,#6a7a40 55%,#7d5a44 80%,#5b3d2e 100%)}

/* services */
.services{left:0;top:1131px;width:1200px;height:647px;background:linear-gradient(180deg,#1e1e1e,#262523 60%,#1b1b1b)}
.cross{position:absolute;background:var(--yellow)}
.services h2{position:absolute;left:0;width:1200px;top:74px;text-align:center;font-family:var(--slab);font-weight:800;font-size:60px;line-height:1.1;color:var(--white)}
.services .intro{position:absolute;left:170px;width:860px;top:166px;text-align:center;font-size:11.2px;line-height:17px;color:var(--white)}
.svc-card{position:absolute;top:228px;width:280px}
.svc-card .img{height:163px}
.svc-card h3{margin-top:22px;font-weight:700;font-size:14px;color:var(--white)}
.svc-card p{margin-top:14px;font-size:11.2px;line-height:17px;color:var(--white);text-align:justify}
.svc-card .btn{margin-top:30px;width:134px;height:46px;border-radius:23px}
.chev{position:absolute;top:277px}

/* benefits */
.benefits-eyebrow{left:0;width:1200px;top:1817px;text-align:center;font-family:var(--slab);font-weight:700;font-size:24px;color:var(--yellow);line-height:1}
.benefits-title{left:0;width:1200px;top:1845px;text-align:center;font-family:var(--slab);font-weight:800;font-size:50px;color:var(--ink);line-height:1}
.band-dark{left:0;top:2183px;width:1200px;height:242px;background:var(--dark)}
.benefit h3{font-family:var(--slab);font-weight:700;font-size:21px;color:var(--ink);letter-spacing:.3px}
.benefit ul{list-style:none;margin-top:28px}
.benefit li{display:flex;align-items:flex-start;gap:8px;font-size:11.8px;line-height:29px;color:#444}
.benefit li svg{margin-top:9px;flex:none}
.benefit.on-dark h3,.benefit.on-dark li{color:var(--white)}
.ins{left:538px;top:1976px;width:500px}
.pto{left:160px;top:2237px;width:500px}
.ret{left:538px;top:2484px;width:500px}
.ret li{line-height:30px}
.img-ins{left:161px;top:1938px;width:335px;height:245px;background:linear-gradient(135deg,#d9dadc,#8a8e98 45%,#3a4660 75%,#c9c6c0)}
.img-pto{left:687px;top:2183px;width:352px;height:242px;background:linear-gradient(135deg,#6e4a2e 0%,#f2dc3a 30%,#f4e24a 65%,#8a5a36 100%)}
.img-ret{left:161px;top:2425px;width:335px;height:240px;background:linear-gradient(135deg,#bfc2c6,#5d6476 45%,#dcd2c4 75%,#9a9a9a)}

/* contact */
.contact{left:0;top:2665px;width:1200px;height:595px;background:var(--light)}
.contact .eyebrow{position:absolute;left:0;width:1200px;top:68px;text-align:center;font-family:var(--slab);font-weight:700;font-size:20px;color:var(--yellow)}
.contact h2{position:absolute;left:0;width:1200px;top:90px;text-align:center;font-family:var(--slab);font-weight:800;font-size:58px;line-height:1.1;color:var(--ink)}
.contact .intro{position:absolute;left:230px;width:740px;top:166px;text-align:center;font-size:11.2px;line-height:17px;color:#555}
.field{position:absolute;border:2px solid #a9a9a9;background:transparent;font-size:11.5px;color:#666;padding:18px 18px}
.submit{position:absolute;left:516px;top:506px;width:168px;height:50px;border-radius:25px;font-size:19px}

/* footer */
.footer{left:0;top:3260px;width:1200px;height:255px;background:var(--dark)}
.footer h4{position:absolute;top:44px;font-family:var(--slab);font-weight:700;font-size:21px;color:var(--white)}
.footer .rule{position:absolute;top:84px;width:34px;height:3px;background:var(--yellow)}
.footer .divider{position:absolute;top:55px;width:1px;height:140px;background:#3a3a3a}
.footer .about{position:absolute;left:161px;top:113px;width:260px;font-size:11.2px;line-height:17.5px;color:var(--white);text-align:justify}
.footer .links{position:absolute;left:566px;top:111px;list-style:none}
.footer .links li{font-size:11.2px;line-height:23.3px;color:var(--white)}
.footer .details{position:absolute;left:806px;top:111px;list-style:none}
.footer .details li{display:flex;gap:14px;font-size:11.2px;line-height:20.5px;color:var(--white)}
.footer .details li svg{flex:none;margin-top:4px}

.copyright{left:0;top:3515px;width:1200px;height:54px;background:var(--yellow)}
.copyright p{position:absolute;left:161px;top:20px;font-size:10px;color:var(--ink)}
.copyright .social-set{position:absolute;left:905px;top:17px;gap:12px}
.copyright .social-set span{background:var(--dark)}
</style>
</head>
<body>

<!-- top bar -->
<div class="abs topbar"></div>
<div class="abs topbar-address">
  <svg width="9" height="12" viewBox="0 0 9 12"><path d="M4.5 0A4.5 4.5 0 0 0 0 4.5C0 8 4.5 12 4.5 12S9 8 9 4.5A4.5 4.5 0 0 0 4.5 0zm0 6.3a1.8 1.8 0 1 1 0-3.6 1.8 1.8 0 0 1 0 3.6z" fill="#fff"/></svg>
  48 Quarry Ridge Road, Orange, CT 06477
</div>
<div class="abs topbar-social"></div>
<div class="abs social-set topbar-icons"><span></span><span></span><span></span><span></span><span></span></div>

<!-- brand -->
<div class="abs brand-box">
  <span class="dot"></span>
  <span class="name">K&amp;T<br>Equipment</span>
</div>

<!-- header contacts -->
<div class="abs contact-chip chip-mail">
  <span class="ring"><svg width="18" height="13" viewBox="0 0 18 13"><rect width="18" height="13" rx="2" fill="#2d2d40"/><path d="M1 1.5 9 7.5 17 1.5" stroke="#fff" stroke-width="1.6" fill="none"/></svg></span>
  <div><div class="label">Mail</div><div class="value">hello@kt-equipment.example</div></div>
</div>
<div class="abs contact-chip chip-phone">
  <span class="ring"><svg width="16" height="16" viewBox="0 0 24 24"><path d="M6.6 10.8a15.1 15.1 0 0 0 6.6 6.6l2.2-2.2a1 1 0 0 1 1-.25 11.4 11.4 0 0 0 3.6.57 1 1 0 0 1 1 1V20a1 1 0 0 1-1 1A17 17 0 0 1 3 4a1 1 0 0 1 1-1h3.5a1 1 0 0 1 1 1c0 1.25.2 2.45.57 3.6a1 1 0 0 1-.25 1z" fill="#2d2d40"/></svg></span>
  <div><div class="label">Phone</div><div class="value">+ 800-555-0142</div></div>
</div>

<!-- nav -->
<nav class="abs mainnav">
  <a style="left:160px">HOME</a>
  <a style="left:309px">ABOUT US</a>
  <a style="left:508px">SERVICES</a>
  <a style="left:676px">EMPLOYEE BENEFIT</a>
  <a style="left:943px">CONTACT US</a>
</nav>

<!-- hero -->
<section class="abs hero" role="img" aria-label="Technician repairing the engine of a red heavy machine">
  <h1>K&amp;T<br>EQUIPMENT CORP</h1>
  <span class="arrow prev"><svg width="10" height="12" viewBox="0 0 10 12"><path d="M7 1 2 6l5 5" stroke="#fff" stroke-width="1.8" fill="none"/></svg></span>
  <span class="arrow next"><svg width="10" height="12" viewBox="0 0 10 12"><path d="M3 1l5 5-5 5" stroke="#fff" stroke-width="1.8" fill="none"/></svg></span>
</section>

<!-- welcome -->
<div class="abs badge">WELCOME TO</div>
<h2 class="abs welcome-title">HEAVY EQUIPMENT<br>SERVICE</h2>
<p class="abs welcome-text">K&amp;T Equipment Corp. is a family owned industry leader that’s been supplying construction equipment, tractors and landscaping gear to Southern Connecticut for the past 81 years. Located on Route 9 in Orange, we help home builders, site excavators, road builders, municipalities, landscapers, home owners and many more. We believe we can make work fun and easy by supplying new and used equipment, equipment rentals, service, parts and advice. Our fast paced service department is ready to expand! We are looking for a Heavy Equipment Service Technician, Experience Required.</p>
<div class="abs btn welcome-btn">Read More</div>
<div class="abs welcome-photo" role="img" aria-label="Operator driving a mini excavator in front of a stone house"></div>

<!-- services -->
<section class="abs services">
  <span class="cross" style="left:358px;top:106px;width:54px;height:1px"></span>
  <span class="cross" style="left:385px;top:86px;width:1px;height:42px"></span>
  <span class="cross" style="left:780px;top:106px;width:52px;height:1px"></span>
  <span class="cross" style="left:805px;top:86px;width:1px;height:42px"></span>
  <h2>SERVICES</h2>
  <p class="intro">Lorem ipsum dolor sit amet, consectetur adipiscing elit. Ut quis laoreet diam. Quisque ac aliquam dui. Praesent pretium quam tellus, quis sollicitudin felis varius et. Vestibulum viverra pulvinar aliquam dui. Praesent pretium quam tellus, quis sollicitudin felis varius et. Vestibulum viverra pulvinar</p>

  <svg class="chev" style="left:70px" width="24" height="44" viewBox="0 0 24 44"><path d="M22 2 2 22l20 20" stroke="#ddd" stroke-width="2" fill="none"/></svg>
  <svg class="chev" style="left:1084px" width="24" height="44" viewBox="0 0 24 44"><path d="M2 2l20 20L2 42" stroke="#fff" stroke-width="2" fill="none"/></svg>

  <article class="svc-card" style="left:161px">
    <div class="img" role="img" aria-label="Mechanics working on a large green tractor" style="background:linear-gradient(135deg,#5f6a58,#8a2f26 50%,#3a3a3a)"></div>
    <h3>LOREM IPSUM DOLO</h3>
    <p>Lorem ipsum dolor sit amet, consectetur adipiscing elit. Ut quis laoreet diam. Quisque ac aliquam dui. Praesent pretium.</p>
    <div class="btn">Read More</div>
  </article>
  <article class="svc-card" style="left:460px">
    <div class="img" role="img" aria-label="Technicians in hard hats servicing an engine" style="background:linear-gradient(135deg,#6c6f74,#c9b24a 40%,#2f3440 75%,#8d8f92)"></div>
    <h3>LOREM IPSUM DOLO</h3>
    <p>Lorem ipsum dolor sit amet, consectetur adipiscing elit. Ut quis laoreet diam. Quisque ac aliquam dui. Praesent pretium.</p>
    <div class="btn">Read More</div>
  </article>
  <article class="svc-card" style="left:758px">
    <div class="img" role="img" aria-label="Red excavator demolishing a house" style="background:linear-gradient(135deg,#9fb0c4,#c2402c 45%,#7a746a 75%,#5e5a52)"></div>
    <h3>LOREM IPSUM DOLO</h3>
    <p>Lorem ipsum dolor sit amet, consectetur adipiscing elit. Ut quis laoreet diam. Quisque ac aliquam dui. Praesent pretium.</p>
    <div class="btn">Read More</div>
  </article>
</section>

<!-- benefits -->
<div class="abs benefits-eyebrow">EMPLOYEE</div>
<h2 class="abs benefits-title">BENEFITS</h2>

<div class="abs img-ins" role="img" aria-label="Two colleagues looking at a laptop together"></div>
<div class="abs benefit ins">
  <h3>INSURANCE BENEFITS</h3>
  <ul>
    <li><svg width="12" height="11" viewBox="0 0 12 11"><rect x=".7" y="1.7" width="8.6" height="8.6" rx="1" stroke="#444" stroke-width="1.2" fill="none"/><path d="M3 5.5l2 2L11 1" stroke="#444" stroke-width="1.6" fill="none"/></svg>Employer Paid, no cost Comprehensive Health Insurance</li>
    <li><svg width="12" height="11" viewBox="0 0 12 11"><rect x=".7" y="1.7" width="8.6" height="8.6" rx="1" stroke="#444" stroke-width="1.2" fill="none"/><path d="M3 5.5l2 2L11 1" stroke="#444" stroke-width="1.6" fill="none"/></svg>Employer Paid, Short Term Disability Insurance</li>
    <li><svg width="12" height="11" viewBox="0 0 12 11"><rect x=".7" y="1.7" width="8.6" height="8.6" rx="1" stroke="#444" stroke-width="1.2" fill="none"/><path d="M3 5.5l2 2L11 1" stroke="#444" stroke-width="1.6" fill="none"/></svg>Optional Dental, Vision, Long Term Disability, Hospitalization and Life Insurance</li>
  </ul>
</div>

<div class="abs band-dark"></div>
<div class="abs benefit on-dark pto">
  <h3>PAID TIME OFF BENEFITS</h3>
  <ul>
    <li><svg width="12" height="11" viewBox="0 0 12 11"><rect x=".7" y="1.7" width="8.6" height="8.6" rx="1" stroke="#fff" stroke-width="1.2" fill="none"/><path d="M3 5.5l2 2L11 1" stroke="#fff" stroke-width="1.6" fill="none"/></svg>Paid Vacation Time (up to 2 weeks based on tenure)</li>
    <li><svg width="12" height="11" viewBox="0 0 12 11"><rect x=".7" y="1.7" width="8.6" height="8.6" rx="1" stroke="#fff" stroke-width="1.2" fill="none"/><path d="M3 5.5l2 2L11 1" stroke="#fff" stroke-width="1.6" fill="none"/></svg>5 Paid Holidays per year</li>
    <li><svg width="12" height="11" viewBox="0 0 12 11"><rect x=".7" y="1.7" width="8.6" height="8.6" rx="1" stroke="#fff" stroke-width="1.2" fill="none"/><path d="M3 5.5l2 2L11 1" stroke="#fff" stroke-width="1.6" fill="none"/></svg>5 Paid Covid Sick Days</li>
  </ul>
</div>
<div class="abs img-pto" role="img" aria-label="Hand holding a yellow sticky note about paid time off"></div>

<div class="abs img-ret" role="img" aria-label="Senior couple reviewing papers on a sofa"></div>
<div class="abs benefit ret">
  <h3>RETIREMENT BENEFITS</h3>
  <ul>
    <li><svg width="12" height="11" viewBox="0 0 12 11"><rect x=".7" y="1.7" width="8.6" height="8.6" rx="1" stroke="#444" stroke-width="1.2" fill="none"/><path d="M3 5.5l2 2L11 1" stroke="#444" stroke-width="1.6" fill="none"/></svg><span>Elective Deferral pre-tax Simple IRA with 100% Employer Match (up to 3% of employee salary)</span></li>
  </ul>
</div>

<!-- contact -->
<section class="abs contact">
  <span class="cross" style="left:327px;top:113px;width:52px;height:1px;opacity:.5"></span>
  <span class="cross" style="left:352px;top:95px;width:1px;height:36px;opacity:.5"></span>
  <span class="cross" style="left:844px;top:113px;width:52px;height:1px;opacity:.5"></span>
  <span class="cross" style="left:869px;top:95px;width:1px;height:36px;opacity:.5"></span>
  <div class="eyebrow">GET IN TOUCH</div>
  <h2>CONTACT US</h2>
  <p class="intro">Lorem ipsum dolor sit amet, consectetur adipiscing elit. Ut consectetur libero id libero ullamcorper mollis. Suspendisse ullamcorper maximus neque sit amet condimentum.</p>
  <div class="field" style="left:161px;top:236px;width:432px;height:53px">Name</div>
  <div class="field" style="left:606px;top:236px;width:432px;height:53px">E-Mail</div>
  <div class="field" style="left:161px;top:304px;width:877px;height:53px">Phone</div>
  <div class="field" style="left:161px;top:380px;width:877px;height:97px">Message</div>
  <div class="btn submit">Submit</div>
</section>

<!-- footer -->
<footer class="abs footer">
  <h4 style="left:161px">ABOUT US</h4><span class="rule" style="left:161px"></span>
  <h4 style="left:566px">QUICK LINK</h4><span class="rule" style="left:566px"></span>
  <h4 style="left:806px">CONTACT DETAILS</h4><span class="rule" style="left:813px"></span>
  <span class="divider" style="left:485px"></span>
  <span class="divider" style="left:763px"></span>
  <p class="about">Lorem ipsum dolor sit amet, consectetur adipiscing elit. Vestibulum feugiat diam est, at pretium diam auctor at. Aliquam in vehicula nisl. Praesent vitae libero suscipit in vehicula nisl. Praesent vitae libero suscipit.</p>
  <ul class="links">
    <li>&gt;&gt; Home</li>
    <li>&gt;&gt; About us</li>
    <li>&gt;&gt; Services</li>
    <li>&gt;&gt; Employee Benefit</li>
    <li>&gt;&gt; Contact us</li>
  </ul>
  <ul class="details">
    <li><svg width="10" height="13" viewBox="0 0 9 12"><path d="M4.5 0A4.5 4.5 0 0 0 0 4.5C0 8 4.5 12 4.5 12S9 8 9 4.5A4.5 4.5 0 0 0 4.5 0zm0 6.3a1.8 1.8 0 1 1 0-3.6 1.8 1.8 0 0 1 0 3.6z" fill="#fff"/></svg><span>48 Quarry Ridge Road, Orange,<br>CT 06477</span></li>
    <li><svg width="12" height="12" viewBox="0 0 24 24"><path d="M6.6 10.8a15.1 15.1 0 0 0 6.6 6.6l2.2-2.2a1 1 0 0 1 1-.25 11.4 11.4 0 0 0 3.6.57 1 1 0 0 1 1 1V20a1 1 0 0 1-1 1A17 17 0 0 1 3 4a1 1 0 0 1 1-1h3.5a1 1 0 0 1 1 1c0 1.25.2 2.45.57 3.6a1 1 0 0 1-.25 1z" fill="#fff"/></svg>+ 800-555-0142</li>
    <li><svg width="14" height="12" viewBox="0 0 14 12"><rect x="1" y="4" width="12" height="7.5" rx="1" stroke="#fff" fill="none"/><rect x="3.5" y=".5" width="7" height="3.5" stroke="#fff" fill="none"/></svg>Fax 203-555-0187</li>
    <li><svg width="14" height="11" viewBox="0 0 18 13"><rect width="18" height="13" rx="2" fill="#fff"/><path d="M1 1.5 9 7.5 17 1.5" stroke="#1c1c1e" stroke-width="1.6" fill="none"/></svg>hello@kt-equipment.example</li>
  </ul>
</footer>

<div class="abs copyright">
  <p>COPYRIGHT © 2022 HEAVY EQUIPMENT SERVICE &nbsp;| &nbsp;ALL RIGHT RESERVED.</p>
  <div class="social-set"><span></span><span></span><span></span><span></span><span></span></div>
</div>

</body>
</html>
```